Retail Seafood business needs package/label design

In need of packaging/label design for multiple seafood products such as sword fish, halibut, cod fish, scallops, mahi, catfish, and lobster tails

```html
<!DOCTYPE html>
<html lang="en">
<head>
<meta charset="UTF-8">
<title>Harbor Lane Market – Yellowfin Tuna Label</title>
<link rel="stylesheet" href="https://fonts.googleapis.com/css2?family=Caveat:wght@500&family=Josefin+Sans:wght@400;600&family=Oswald:wght@400&display=swap">
<style>
  :root {
    --mint: #bdf8ea;
    --navy: #3d4c78;
    --teal: #69a9b8;
    --teal-light: #9fcad4;
    --cream: #f8f6f2;
    --paper: #f1f4f5;
    --paper-shade: #e3ebee;
    --copper: #b0806d;
    --beige: #e6dfd4;
  }
  * { margin: 0; padding: 0; box-sizing: border-box; }
  html, body { width: 1200px; height: 728px; overflow: hidden; }
  body {
    background: var(--mint);
    position: relative;
    font-family: "Josefin Sans", sans-serif;
  }
  .label {
    position: absolute;
    left: 424px; top: 20px;
    width: 351px; height: 687px;
    overflow: hidden;
    box-shadow: 0 2px 8px rgba(40, 80, 80, 0.12);
  }
  .label__wave-texture {
    position: absolute; inset: 0;
    background: linear-gradient(160deg, var(--paper) 0%, var(--paper-shade) 50%, var(--paper) 100%);
  }
  .label__shapes { position: absolute; inset: 0; }
  .abs { position: absolute; left: 0; width: 100%; text-align: center; }
  .brand-name {
    font-family: "Josefin Sans", sans-serif;
    font-weight: 600;
    color: var(--beige);
    letter-spacing: 1px;
  }
  .brand-name--top { top: 58px; font-size: 22px; line-height: 26px; }
  .tagline {
    top: 134px;
    font-size: 7px; line-height: 8px;
    letter-spacing: 1.6px;
    color: var(--beige);
  }
  .product-title {
    top: 254px;
    font-family: "Oswald", sans-serif;
    font-weight: 400;
    font-size: 38px; line-height: 40px;
    letter-spacing: 1.5px;
    color: var(--beige);
  }
  .category {
    top: 316px;
    font-family: "Caveat", cursive;
    font-weight: 500;
    font-size: 27px; line-height: 30px;
    color: var(--beige);
  }
  .pricing {
    top: 419px;
    font-size: 8px; letter-spacing: 1.2px;
    color: var(--navy); font-weight: 600;
  }
  .claim {
    top: 443px;
    font-size: 9.5px; letter-spacing: 1.3px;
    color: var(--navy); font-weight: 600;
  }
  .grade {
    top: 467px;
    font-size: 7.5px; line-height: 10.5px; letter-spacing: 1.1px;
    color: var(--navy); font-weight: 600;
  }
  .brand-name--bottom {
    left: 79px; width: 192px;
    top: 532px;
    font-size: 13px; line-height: 16px;
    letter-spacing: 0.6px;
    white-space: nowrap;
  }
  .address {
    top: 589px;
    font-size: 7.5px; line-height: 11px; letter-spacing: 0.8px;
    color: var(--copper); font-weight: 600;
    font-style: normal;
  }
  .website {
    top: 634px;
    font-size: 8.5px; letter-spacing: 0.4px;
    color: var(--navy);
  }
  .socials {
    position: absolute; left: 0; top: 664px; width: 100%;
    display: flex; justify-content: space-around;
    padding: 0 18px;
    font-size: 8.5px; color: var(--cream);
  }
  .social { display: flex; align-items: center; gap: 4px; }
  .social__dot {
    width: 9px; height: 9px; border-radius: 50%;
    background: var(--navy);
  }
</style>
</head>
<body>
  <main class="label">
    <div class="label__wave-texture" role="img" aria-label="Fine wavy line pattern across the label background"></div>

    <svg class="label__shapes" width="351" height="687" viewBox="0 0 351 687" aria-hidden="true">
      <rect class="info-panel" x="42" y="46" width="266" height="457" fill="var(--cream)" stroke="var(--copper)" stroke-width="1.2"/>
      <path class="banner" d="M78 0 H272 V353 L175 382 L78 353 Z" fill="var(--navy)"/>
      <path class="banner-edge" d="M78 307 V353 L175 382 L272 353 V307" fill="none" stroke="var(--copper)" stroke-width="1.2"/>
      <rect class="title-ribbon" x="0" y="241" width="351" height="66" fill="var(--teal)"/>
      <line x1="0" y1="245" x2="351" y2="245" stroke="var(--teal-light)" stroke-width="1"/>
      <line x1="0" y1="303" x2="351" y2="303" stroke="var(--teal-light)" stroke-width="1"/>
      <line x1="61" y1="438" x2="288" y2="438" stroke="var(--copper)" stroke-width="0.6" opacity="0.6"/>
      <line x1="61" y1="458" x2="288" y2="458" stroke="var(--copper)" stroke-width="0.6" opacity="0.6"/>
      <rect class="footer-brand" x="79" y="503" width="192" height="75" fill="var(--navy)"/>
      <path d="M79 503 V578 H271 V503" fill="none" stroke="var(--copper)" stroke-width="1.2"/>
      <rect class="social-bar" x="0" y="655" width="351" height="32" fill="var(--teal)"/>
      <line x1="0" y1="655" x2="351" y2="655" stroke="var(--copper)" stroke-width="1.5"/>
    </svg>

    <div class="abs brand-name brand-name--top">HARBOR LANE<br>MARKET</div>
    <p class="abs tagline">THE MIDWEST'S SOURCE OF<br>SEAFOOD &amp; PRODUCE<br>FOR OVER 15 YEARS</p>

    <h1 class="abs product-title">YELLOWFIN TUNA</h1>
    <p class="abs category">fresh Seafood</p>

    <p class="abs pricing">PRICED PER POUND</p>
    <p class="abs claim">SOME OF THE BEST TUNA YOU CAN EAT</p>
    <p class="abs grade">#1 SASHIMI GRADE<br>WILD CAUGHT</p>

    <div class="abs brand-name brand-name--bottom">HARBOR LANE MARKET</div>

    <address class="abs address">218 W. LARKFIELD AVE<br>CHICAGO, IL 60655<br>312-555-0186</address>
    <p class="abs website">www.harborlanemarket.com/</p>

    <div class="socials">
      <span class="social"><span class="social__dot"></span>harborlane_mkt</span>
      <span class="social"><span class="social__dot"></span>@harborlanemkt</span>
      <span class="social"><span class="social__dot"></span>@harborlanemkt</span>
    </div>
  </main>
</body>
</html>
```